Stationery Design Project for Velmora, Chicago

Velmora, a street parking application which helps car drivers find a street parking spot by offering an ideal path along which to look for parking. This path is calculated by our algorithm based on data (e.g. historical data, baseball games schedule, etc.). Along this path the driver will find a spot and will also save 70% of the search time. Customer we target is reg. between 21 and 45 yo.

We envision something young, fresh, bright and original. Slightly abstract maybe. It should represent the idea and elements of finding street parking in the city, e.g. car(s), parking spot, people, city, etc. (just ideas!).

Logo is attached.

Requirement:
- Business Cards (2 Sided Full Color CMYK)
- Letterhead (1 Sided Full Color CMYK)
- Envelope (1 Sided Full Color CMYK)
- Sticker (1 Sided Full Color CMYK), round with a 2inch diameter.
Updates

Reason: We're starting to get more and more designs and need more time to look into all of them. Very exciting!! Thanks to everybody!

Hi all, we're in the process of selecting our favs. Though choices!!! Really good submissions. Will keep you posted and sorry for the delay.

Target Market(s)

Car drivers and owners between 21 and 45

Industry/Entity Type

Parking

Requirements
Must have
• Sticker should be round and include company URL velmora.com and the new logo which we will attach soon.
Should not have
• Should not be too serious or boring.

```html
<!DOCTYPE html>
<html lang="en">
<head>
<meta charset="utf-8">
<title>Velmora Stationery</title>
<link rel="stylesheet" href="https://fonts.googleapis.com/css2?family=Comfortaa:wght@400;700&family=Open+Sans:wght@400;600&display=swap">
<style>
  :root {
    --bg: #e6e8eb;
    --paper: #ffffff;
    --ink: #1c1c1e;
    --brand-blue: #1a78c8;
    --brand-deep: #0e3f74;
    --brand-navy: #0a2f5c;
    --sky: #3aa8e4;
    --silver: #c9ced4;
    --muted: #4a4f57;
    --band: #0d0d0f;
  }
  * { box-sizing: border-box; margin: 0; padding: 0; }
  html, body { width: 1200px; height: 1200px; overflow: hidden; }
  body {
    background: var(--bg);
    position: relative;
    font-family: "Comfortaa", "Open Sans", sans-serif;
    color: var(--ink);
  }
  .piece { position: absolute; background: var(--paper); box-shadow: 0 6px 18px rgba(0,0,0,.12); overflow: hidden; }

  /* brand lockup */
  .brand { display: flex; align-items: center; gap: 10px; }
  .brand-dot {
    border-radius: 50%;
    background: var(--brand-blue);
    border: 3px solid #fff;
    box-shadow: 0 0 0 1px var(--silver);
    flex: none;
  }
  .brand-name { font-family: "Comfortaa", sans-serif; font-weight: 700; color: var(--ink); letter-spacing: .5px; }

  /* letterhead */
  .letterhead { left: 60px; top: 190px; width: 580px; height: 820px; }
  .letterhead .pattern {
    position: absolute; inset: 0 0 70px 0;
    background: radial-gradient(ellipse at 55% 55%, #e9eaec 0%, #f6f6f7 40%, #ffffff 75%);
  }
  .letterhead .brand { position: absolute; top: 52px; left: 0; right: 0; justify-content: center; }
  .letterhead .brand-dot { width: 62px; height: 62px; }
  .letterhead .brand-name { font-size: 44px; }
  .letterhead .footer {
    position: absolute; left: 0; right: 0; bottom: 0; height: 70px;
    background: linear-gradient(180deg, #3a3a3d 0%, var(--band) 30%, var(--band) 100%);
    color: #fff; font-family: "Open Sans", sans-serif; font-size: 10px;
    text-align: center; line-height: 1.55; padding-top: 20px;
  }

  /* envelope */
  .envelope { left: 680px; top: 60px; width: 460px; height: 212px; }
  .envelope .brand { position: absolute; top: 26px; left: 32px; }
  .envelope .brand-dot { width: 40px; height: 40px; }
  .envelope .brand-name { font-size: 28px; }
  .envelope .address {
    position: absolute; top: 80px; left: 60px; width: 170px;
    font-size: 9px; text-align: center; line-height: 1.5; color: var(--ink);
  }

  /* business card front */
  .card { width: 420px; height: 240px; }
  .card-front { left: 700px; top: 310px;
    background: radial-gradient(ellipse at 50% 20%, #2a6fb4 0%, var(--brand-deep) 55%, var(--brand-navy) 100%); }
  .card-front .dome {
    position: absolute; left: 60px; top: -150px; width: 300px; height: 300px; border-radius: 50%;
    background: radial-gradient(circle at 50% 40%, #ffffff 40%, #e3e6ea 80%, #cfd4da 100%);
    border: 4px solid var(--silver);
    box-shadow: 0 6px 16px rgba(0,0,0,.35);
  }
  .card-front .brand { position: absolute; top: 18px; left: 0; right: 0; justify-content: center; }
  .card-front .brand-dot { width: 42px; height: 42px; }
  .card-front .brand-name { font-size: 30px; }
  .card-front .person { position: absolute; top: 90px; left: 0; right: 0; text-align: center; }
  .card-front .person-name { font-weight: 700; font-size: 12px; color: var(--ink); }
  .card-front .person-role { font-size: 8px; color: var(--brand-blue); margin-top: 2px; }
  .card-front .contact {
    position: absolute; left: 0; right: 0; bottom: 22px; text-align: center;
    color: #fff; font-size: 8px; line-height: 1.6;
  }

  /* business card back */
  .card-back { left: 700px; top: 580px; background: radial-gradient(circle at 50% 50%, #3a3a3d 0%, #0c0c0d 70%); }
  .card-back .orb {
    position: absolute; left: 122px; top: 33px; width: 176px; height: 176px; border-radius: 50%;
    border: 5px solid var(--silver);
    background: radial-gradient(circle at 50% 35%, #7cd0f5 0%, var(--sky) 45%, #1766a8 100%);
    display: flex; align-items: center; justify-content: center;
    box-shadow: 0 0 0 2px #555, 0 6px 14px rgba(0,0,0,.6);
  }
  .card-back .url { font-weight: 700; font-size: 10px; color: var(--ink); }

  /* stickers */
  .sticker {
    position: absolute; width: 200px; height: 200px; border-radius: 50%;
    background: var(--paper); box-shadow: 0 6px 16px rgba(0,0,0,.18);
    display: flex; align-items: center; justify-content: center;
  }
  .sticker-disc {
    width: 164px; height: 164px; border-radius: 50%; border: 4px solid var(--silver);
    display: flex; align-items: center; justify-content: center;
  }
  .sticker-name { left: 700px; top: 860px; }
  .sticker-name .sticker-disc { background: radial-gradient(circle at 50% 35%, #6cc6f2 0%, var(--sky) 45%, #145f9e 100%); }
  .sticker-name .label { font-weight: 700; font-size: 26px; color: #fff; }
  .sticker-url { left: 940px; top: 860px; }
  .sticker-url .sticker-disc { background: radial-gradient(circle at 50% 35%, #4a8ff0 0%, #1c56c8 50%, #0f2f86 100%); }
  .sticker-url .label { font-weight: 700; font-size: 17px; color: #fff; }
</style>
</head>
<body>

  <section class="piece letterhead">
    <div class="pattern" role="img" aria-label="Faint grey circuit-line pattern across the sheet"></div>
    <div class="brand"><span class="brand-dot"></span><span class="brand-name">velmora</span></div>
    <div class="footer">
      <p>dummy dummy, dummy dummy City, dummy Country dummy</p>
      <p>+1 312 555 0142 | (312) 555 0178 | (312) 555 0193 | www.northlane.com | alex@northlane.com</p>
    </div>
  </section>

  <section class="piece envelope">
    <div class="brand"><span class="brand-dot"></span><span class="brand-name">velmora</span></div>
    <div class="address">
      <p>dummy City dummy</p>
      <p>Country land dummy dummy</p>
    </div>
  </section>

  <section class="piece card card-front">
    <div class="dome">
    </div>
    <div class="brand"><span class="brand-dot"></span><span class="brand-name">velmora</span></div>
    <div class="person">
      <p class="person-name">Alex REED</p>
      <p class="person-role">Director</p>
    </div>
    <div class="contact">
      <p>dummy dummy, dummy dummy City, dummy Country dummy</p>
      <p>+1 312 555 0142 | (312) 555 0178 | (312) 555 0193 | alex@velmora.com</p>
    </div>
  </section>

  <section class="piece card card-back">
    <div class="orb"><span class="url">www.velmora.com</span></div>
  </section>

  <div class="sticker sticker-name">
    <div class="sticker-disc"><span class="label">velmora</span></div>
  </div>
  <div class="sticker sticker-url">
    <div class="sticker-disc"><span class="label">velmora.com</span></div>
  </div>

</body>
</html>
```